Lowell Brandt

20 Year Licensed Master Barber specializing in:
men/women cuts, Grooming, Straight razor Shaving and tape line enhancement, beard grooming, eye brow enhancement, South of France, Hot Towel Treatments, Scalp, Blow outs, Shags, Custom Design,RazorCuts,Shear Cuts, Bobs, Perms, Relaxers, Shoe Shine.
Please create a wonderful business card incorporating all the info above and selecting one of the photos. Please be creative.

Barber

```html
<!DOCTYPE html>
<html lang="en">
<head>
<meta charset="utf-8">
<title>Lowell Brandt – Master Barber Business Card</title>
<link rel="stylesheet" href="https://fonts.googleapis.com/css2?family=Open+Sans:wght@400;600&family=Playball&display=swap">
<style>
  :root {
    --backdrop: #7a5a36;
    --card-black: #0b0b0c;
    --card-sheen: #1c1c1f;
    --barber-red: #d8202e;
    --barber-red-dark: #a3141f;
    --ink-white: #ffffff;
    --ink-soft: #e9e9e9;
    --seal-ink: #1f3a7a;
    --photo-warm: #9a6a55;
    --photo-light: #d8a98c;
  }
  * { box-sizing: border-box; margin: 0; padding: 0; }
  html, body { width: 1200px; height: 1023px; overflow: hidden; }
  body {
    background: var(--backdrop);
    display: flex; flex-direction: column; align-items: center; justify-content: center;
    gap: 40px;
    font-family: "Open Sans", Arial, sans-serif;
  }
  .card {
    position: relative; width: 820px; height: 469px; overflow: hidden;
    background: linear-gradient(160deg, var(--card-sheen) 0%, var(--card-black) 55%);
    border-radius: 6px;
    box-shadow: 0 10px 24px rgba(0,0,0,.45);
  }
  .card-band { position: absolute; left: 0; bottom: 0; width: 820px; height: 200px; }

  /* front */
  .portrait {
    position: absolute; right: 22px; top: 22px; width: 400px; height: 270px;
    background: linear-gradient(120deg, var(--photo-warm) 0%, var(--photo-light) 70%);
  }
  .contact-list {
    position: absolute; left: 44px; top: 70px; list-style: none;
    color: var(--ink-soft); font-size: 22px; line-height: 1.55;
  }
  .identity { position: absolute; left: 420px; top: 300px; color: var(--ink-white); }
  .identity-name { font-family: "Playball", cursive; font-size: 50px; font-weight: 400; line-height: 1; }
  .identity-role { font-size: 24px; font-weight: 600; margin-top: 4px; padding-left: 40px; }
  .seal {
    position: absolute; left: 238px; top: 318px; width: 130px; height: 130px; border-radius: 50%;
    background: var(--ink-white); border: 6px solid var(--card-black);
    display: flex; align-items: center; justify-content: center; text-align: center;
    color: var(--seal-ink); font-size: 19px; font-weight: 600; line-height: 1.15;
  }

  /* back */
  .services-title {
    position: absolute; left: 60px; top: 46px;
    color: var(--barber-red); font-size: 30px; font-weight: 600;
  }
  .services-list {
    position: absolute; left: 60px; top: 104px; width: 700px;
    columns: 3; column-gap: 24px; list-style: none;
    color: var(--ink-soft); font-size: 15px; line-height: 1.5;
  }
  .services-list li::before { content: "• "; color: var(--ink-white); }
  .back-disc {
    position: absolute; left: 350px; top: 308px; width: 120px; height: 120px; border-radius: 50%;
    background: var(--ink-white); border: 6px solid var(--card-black);
  }
</style>
</head>
<body>

<section class="card card-front">
  <div class="portrait" role="img" aria-label="Portrait photo of the barber wearing a tweed flat cap and glasses"></div>
  <ul class="contact-list">
    <li>lowell.brandt7@mailpost.com</li>
    <li>(555)318-4410</li>
    <li>Snapfeed:lbrandtcuts</li>
    <li>Friendbook:YourFriendbook</li>
  </ul>
  <svg class="card-band" viewBox="0 0 820 200" aria-hidden="true">
    <path d="M0 60 Q400 150 820 70 L820 200 L0 200 Z" fill="var(--card-black)"/>
    <path d="M0 78 Q400 168 820 88 L820 200 L0 200 Z" fill="var(--barber-red)"/>
    <path d="M0 120 Q400 200 820 130 L820 200 L0 200 Z" fill="var(--barber-red-dark)" opacity=".35"/>
  </svg>
  <div class="seal">Lowell<br>Brandt</div>
  <div class="identity">
    <h1 class="identity-name">Lowell Brandt</h1>
    <p class="identity-role">Master Barber</p>
  </div>
</section>

<section class="card card-back">
  <h2 class="services-title">Specializing in</h2>
  <ul class="services-list">
    <li>Men/Women Cuts</li>
    <li>Grooming</li>
    <li>Straight Razor Shaving</li>
    <li>Tape Line Enhancement</li>
    <li>Beard Grooming</li>
    <li>Eye Brow Enhancement</li>
    <li>South of France</li>
    <li>Hot Towel Treatments</li>
    <li>Scalp</li>
    <li>Blow Outs</li>
    <li>Shags</li>
    <li>Custom Design</li>
    <li>Razor Cuts</li>
    <li>Shear Cuts</li>
    <li>Bobs</li>
    <li>Perms</li>
    <li>Relaxers</li>
    <li>Shoe Shine</li>
  </ul>
  <svg class="card-band" viewBox="0 0 820 200" aria-hidden="true">
    <path d="M0 60 Q400 150 820 70 L820 200 L0 200 Z" fill="var(--card-black)"/>
    <path d="M0 78 Q400 168 820 88 L820 200 L0 200 Z" fill="var(--barber-red)"/>
    <path d="M0 120 Q400 200 820 130 L820 200 L0 200 Z" fill="var(--barber-red-dark)" opacity=".35"/>
  </svg>
  <div class="back-disc"></div>
</section>

</body>
</html>
```